Steady Harbour Coaching Business Card

We need a business card for a new business based in Sydney Australia called "Steady Harbour Coaching". The business provides the following:
1. Resilience systems for individuals - Developing personalised resilience programs that increase stress tolerance, improve work effectiveness and minimise stress responses to challenge.
2. Group Resilience Training for Leaders and managers - Delivering Resilience training packages and ongoing support to leadership cadres within organisations.
3. High Risk Resilience Training - providing resilience training for High Risk professions such as emergency responders, military and police.

Target Market(s)

Corporate / Military / Emergency Responders

Industry/Entity Type

Leadership

Contact Information for Business Card

Steady Harbour Coaching, Derek Falwood, 7/19 Kestrel St Penbrook 2093, quiet.morning.tide@mailpost.example, www.steadyharbourcoaching.example.au, M# 0417603842
Personalised Mental Resilience Systems for leaders and high risk professions

Requirements
Must have
• 1. Creation of a logo/graphic - to include 3 elements:
a. Military
b.Corporate
c. Emergency Responder.

As long as those 3 elements are included - I am open to any potential designs. Preference given to those who can create a logo out of the above three elements.

```html
<!DOCTYPE html>
<html lang="en">
<head>
<meta charset="utf-8">
<title>Steady Harbour Coaching – Business Card</title>
<link rel="stylesheet" href="https://fonts.googleapis.com/css2?family=Open+Sans:wght@400;600&display=swap">
<style>
  :root {
    --page-bg: #e9e6e1;
    --card-white: #ffffff;
    --card-grey: #e4e4e4;
    --panel-dark: #1c1c1c;
    --panel-mid: #4a4a4a;
    --text-dark: #2a2a2a;
    --text-name: #555555;
    --text-light: #f4f4f4;
  }
  * { margin: 0; padding: 0; box-sizing: border-box; }
  html, body {
    width: 1200px;
    height: 1022px;
    overflow: hidden;
    background: var(--page-bg);
    font-family: "Open Sans", Arial, sans-serif;
  }
  .card {
    position: absolute;
    left: 100px;
    top: 225px;
    width: 1000px;
    height: 572px;
    display: flex;
    background: linear-gradient(160deg, var(--card-white) 0%, var(--card-white) 45%, var(--card-grey) 100%);
    box-shadow: 0 14px 30px rgba(0,0,0,0.25);
    overflow: hidden;
  }
  .brand-panel {
    width: 380px;
    height: 100%;
    background: linear-gradient(200deg, var(--panel-mid) 0%, var(--panel-dark) 70%);
    display: flex;
    flex-direction: column;
    align-items: center;
    padding-top: 60px;
  }
  .brand-figures {
    width: 260px;
    height: 250px;
    border-radius: 6px;
    background: radial-gradient(ellipse at 50% 45%, #d8d8d8 0%, #8a8a8a 45%, rgba(40,40,40,0) 75%);
  }
  .brand-name {
    margin-top: 52px;
    color: var(--text-light);
    font-size: 38px;
    font-weight: 400;
    line-height: 1.3;
    text-align: center;
  }
  .details {
    flex: 1;
    position: relative;
    padding: 40px 44px 0 46px;
  }
  .person-name {
    text-align: right;
    color: var(--text-name);
    font-size: 40px;
    font-weight: 400;
  }
  .contact-list {
    list-style: none;
    margin-top: 34px;
  }
  .contact-item {
    display: flex;
    align-items: center;
    gap: 16px;
    color: var(--text-dark);
    font-size: 25px;
    line-height: 1;
    margin-bottom: 30px;
  }
  .contact-icon {
    width: 24px;
    height: 24px;
    flex: none;
    fill: var(--text-dark);
  }
  .tagline {
    position: absolute;
    right: 44px;
    bottom: 46px;
    text-align: right;
    color: var(--text-dark);
    font-size: 25px;
    line-height: 1.55;
  }
</style>
</head>
<body>
  <div class="card">
    <div class="brand-panel">
      <div class="brand-figures" role="img" aria-label="White silhouettes of a soldier, a corporate professional and an emergency responder standing in a row"></div>
      <div class="brand-name">Steady Harbour<br>Coaching</div>
    </div>
    <div class="details">
      <div class="person-name">Derek Falwood</div>
      <ul class="contact-list">
        <li class="contact-item">
          <svg class="contact-icon" viewBox="0 0 24 24" aria-hidden="true"><path d="M12 2a7 7 0 0 0-7 7c0 5 7 13 7 13s7-8 7-13a7 7 0 0 0-7-7zm0 9.5A2.5 2.5 0 1 1 12 6.5a2.5 2.5 0 0 1 0 5z"/></svg>
          <span>7/19 Kestrel St Penbrook 2093,</span>
        </li>
        <li class="contact-item">
          <svg class="contact-icon" viewBox="0 0 24 24" aria-hidden="true"><path d="M6.6 10.8a15 15 0 0 0 6.6 6.6l2.2-2.2a1 1 0 0 1 1-.25 11.4 11.4 0 0 0 3.6.57 1 1 0 0 1 1 1V20a1 1 0 0 1-1 1A17 17 0 0 1 3 4a1 1 0 0 1 1-1h3.5a1 1 0 0 1 1 1c0 1.25.2 2.45.57 3.6a1 1 0 0 1-.25 1z"/></svg>
          <span>0417603842</span>
        </li>
        <li class="contact-item">
          <svg class="contact-icon" viewBox="0 0 24 24" aria-hidden="true"><path d="M2 5h20v14H2z M3.5 6.5 12 13l8.5-6.5" fill="none" stroke="#2a2a2a" stroke-width="2"/><path d="M2 5h20L12 13z"/></svg>
          <span>quiet.morning.tide@mailpost.example</span>
        </li>
        <li class="contact-item">
          <svg class="contact-icon" viewBox="0 0 24 24" aria-hidden="true"><circle cx="12" cy="12" r="10"/><path d="M2 12h20M12 2c3 3 3 17 0 20M12 2c-3 3-3 17 0 20M4 7h16M4 17h16" fill="none" stroke="#ffffff" stroke-width="1.4"/></svg>
          <span>www.steadyharbourcoaching.example.au</span>
        </li>
      </ul>
      <p class="tagline">Personalised Mental Resilience Systems for<br>Leaders and High Risk Professions</p>
    </div>
  </div>
</body>
</html>
```